Email header design .

We require an email header based on the attached design. <br/>- instead of 'internal use only' it should read - 'Velmora ANZ'<br/>- please make the design "pop" more than the attached image, we are open to variations on the relative sizing of the two elements of the design (the field update and the velmora section). <br/>- Colour scheme as per velmora webstie - https://www.velmora-example.com/<br/>

Colors

Designer to choose colors to be used in the design.

```html
<!DOCTYPE html>
<html lang="en">
<head>
<meta charset="utf-8">
<title>Velmora ANZ — Field Update</title>
<link rel="stylesheet" href="https://fonts.googleapis.com/css2?family=Alegreya:wght@400;700;800&family=Alegreya+Sans:wght@500;700&display=swap">
<style>
  :root {
    --backdrop: #bdc1c9;
    --header-bg: #f6f7f9;
    --body-top: #e9e9ea;
    --body-bottom: #dedfe1;
    --navy: #12305e;
    --navy-deep: #0b2248;
    --accent: #2f7fc1;
    --slate: #3c5266;
    --white: #ffffff;
  }
  * { margin: 0; padding: 0; box-sizing: border-box; }
  html, body {
    width: 1200px;
    height: 1200px;
    overflow: hidden;
    background: var(--backdrop);
  }
  .email {
    position: absolute;
    left: 204px;
    top: 64px;
    width: 792px;
    height: 1136px;
    background: linear-gradient(180deg, var(--body-top) 0%, var(--body-bottom) 100%);
    box-shadow: 0 6px 24px rgba(18, 48, 94, 0.18);
  }
  .email-header {
    position: relative;
    height: 122px;
    display: flex;
    background: var(--header-bg);
    border-bottom: 6px solid var(--navy);
  }
  .brand {
    width: 417px;
    display: flex;
    align-items: center;
    padding-left: 40px;
    padding-top: 2px;
  }
  .brand-mark {
    width: 14px;
    height: 14px;
    background: var(--accent);
    margin-right: 14px;
    margin-top: 6px;
  }
  .brand-name {
    font-family: "Alegreya Sans", sans-serif;
    font-weight: 700;
    font-size: 46px;
    color: var(--navy);
    letter-spacing: -0.5px;
  }
  .brand-region {
    font-family: "Alegreya", serif;
    font-size: 25px;
    color: var(--slate);
    margin-left: 8px;
    margin-top: 8px;
  }
  .title-panel {
    position: relative;
    flex: 1;
    display: flex;
    align-items: center;
    justify-content: center;
    background: linear-gradient(135deg, var(--navy) 0%, var(--navy-deep) 100%);
  }
  .title-notch {
    position: absolute;
    left: 0;
    top: 45px;
    width: 14px;
    height: 26px;
  }
  .title {
    font-family: "Alegreya", serif;
    font-weight: 800;
    font-size: 34px;
    color: var(--white);
    letter-spacing: 0.3px;
    padding-top: 2px;
  }
  .title-rule {
    position: absolute;
    left: 50%;
    bottom: 26px;
    width: 56px;
    height: 3px;
    margin-left: -28px;
    background: var(--accent);
  }
</style>
</head>
<body>
  <main class="email">
    <header class="email-header">
      <div class="brand">
        <span class="brand-mark" aria-hidden="true"></span>
        <span class="brand-name">Velmora</span>
        <span class="brand-region">/ anz</span>
      </div>
      <div class="title-panel">
        <svg class="title-notch" viewBox="0 0 14 26" aria-hidden="true">
          <polygon points="0,0 14,13 0,26" fill="var(--header-bg)"/>
        </svg>
        <h1 class="title">Field Update</h1>
        <span class="title-rule" aria-hidden="true"></span>
      </div>
    </header>
  </main>
</body>
</html>
```